Luxury Face Oil Label

I'm looking for a simple and sophisticated design for a natural face oil that will target the luxe market. It is a pure Natural product. I have attached the logo, Velumi Organics.

Here's the Copy

LUXE FACIAL OIL

Regenerate. Hydrate. Glow

100% Natural

30ml (1.01 oz)

A complex blend of Pure Oils including Marula, Sea Buckthorn, Rosehip, Neroli, Evening primrose, Argan, Calendula, Lavender, Jojoba, Grapeseed, Baobab, Moringa and Vitamin E oil.

Produced by
Brasso Kettle Ltd
P.O box 7925-00300
Nairobi, Kenya
www.velumiorganics.example

Target Market(s)

High end

Requirements
Must have
• Simple, Please consider the bottle, which is a 30ml clear glass bottle with a gold and white pump. Image attached.
Nice to have
• Very clean designs, not too much going on.
Should not have
• Leaves and nuts.

```html
<!DOCTYPE html>
<html lang="en">
<head>
<meta charset="utf-8">
<title>Velumi Organics – Luxe Facial Oil Label</title>
<link rel="stylesheet" href="https://fonts.googleapis.com/css2?family=Montserrat:wght@400;500;800&display=swap">
<style>
  :root {
    --page-bg: #f0f0f0;
    --label-bg: #ffffff;
    --gold-dark: #b7841a;
    --gold-mid: #d9ab3e;
    --gold-light: #f5dc84;
    --text-grey: #4a4a4a;
    --text-dark: #2b2b2b;
    --ribbon-text: #ffffff;
  }
  * { margin: 0; padding: 0; box-sizing: border-box; }
  html, body {
    width: 1200px;
    height: 1000px;
    overflow: hidden;
    background: var(--page-bg);
    font-family: "Montserrat", sans-serif;
  }
  .canvas {
    position: relative;
    width: 1200px;
    height: 1000px;
  }
  .label {
    position: absolute;
    left: 50px;
    top: 183px;
    width: 1100px;
    height: 634px;
    background: var(--label-bg);
    box-shadow: 0 10px 30px rgba(0, 0, 0, 0.08);
    overflow: hidden;
  }
  .foliage {
    position: absolute;
    border-radius: 50%;
    opacity: 0.55;
  }
  .foliage--top-left {
    left: 0; top: 24px; width: 251px; height: 163px;
    background: radial-gradient(ellipse at center, var(--gold-light) 0%, rgba(245, 220, 132, 0.35) 50%, rgba(255, 255, 255, 0) 72%);
  }
  .foliage--bottom-right {
    left: 789px; top: 293px; width: 310px; height: 178px;
    background: radial-gradient(ellipse at center, var(--gold-light) 0%, rgba(245, 220, 132, 0.35) 50%, rgba(255, 255, 255, 0) 72%);
  }
  .brand {
    position: absolute;
    left: 221px; top: 88px; width: 340px; height: 284px;
    display: flex;
    flex-direction: column;
    align-items: center;
    justify-content: center;
    gap: 26px;
  }
  .brand__square {
    width: 120px; height: 120px;
    background: var(--gold-mid);
  }
  .brand__name {
    font-weight: 500;
    font-size: 20px;
    line-height: 1;
    letter-spacing: 0.14em;
    text-transform: uppercase;
    white-space: nowrap;
    color: var(--gold-dark);
    text-align: center;
  }
  .front {
    position: absolute;
    left: 191px; width: 400px;
    text-align: center;
    white-space: nowrap;
    line-height: 1;
  }
  .front__title {
    top: 385px;
    font-weight: 800;
    font-size: 30px;
    color: var(--gold-dark);
  }
  .front__tagline {
    top: 436px;
    font-weight: 400;
    font-size: 21px;
    color: var(--text-grey);
  }
  .front__claim {
    top: 473px;
    font-weight: 800;
    font-size: 31px;
    color: var(--gold-dark);
  }
  .ribbon {
    position: absolute;
    height: 48px;
  }
  .ribbon svg {
    position: absolute; inset: 0;
    width: 100%; height: 100%;
  }
  .ribbon__text {
    position: relative;
    display: flex;
    align-items: center;
    justify-content: center;
    height: 100%;
    font-weight: 400;
    font-size: 21px;
    white-space: nowrap;
    color: var(--ribbon-text);
  }
  .ribbon--volume { left: 287px; top: 523px; width: 208px; }
  .ribbon--ingredients { left: 727px; top: 91px; width: 206px; }
  .ingredients {
    position: absolute;
    left: 630px; top: 150px; width: 400px;
    text-align: center;
    font-size: 21px;
    line-height: 26px;
    color: var(--text-grey);
  }
  .producer {
    position: absolute;
    left: 680px; top: 496px; width: 300px;
    text-align: center;
    font-size: 16px;
    line-height: 19.5px;
    color: var(--text-dark);
  }
</style>
</head>
<body>
<div class="canvas">
  <section class="label">
    <svg width="0" height="0" aria-hidden="true" style="position:absolute">
      <defs>
        <linearGradient id="gold-sheen" x1="0" y1="0" x2="1" y2="0">
          <stop offset="0" stop-color="#b7841a"/>
          <stop offset="0.5" stop-color="#f3d77a"/>
          <stop offset="1" stop-color="#b7841a"/>
        </linearGradient>
      </defs>
    </svg>

    <div class="foliage foliage--top-left" role="img" aria-label="Gold line-art leafy branch ornament"></div>
    <div class="foliage foliage--bottom-right" role="img" aria-label="Gold line-art leafy branch ornament"></div>

    <div class="brand">
      <div class="brand__square"></div>
      <div class="brand__name">Velumi Organics</div>
    </div>

    <h1 class="front front__title">LUXE FACIAL OIL</h1>
    <p class="front front__tagline">Regenerate. Hydrate. Glow</p>
    <p class="front front__claim">100% Natural</p>

    <div class="ribbon ribbon--volume">
      <svg viewBox="0 0 208 48" preserveAspectRatio="none" aria-hidden="true">
        <polygon points="0,0 208,0 190,24 208,48 0,48 18,24" fill="url(#gold-sheen)"/>
      </svg>
      <span class="ribbon__text">30ml (1.01 oz)</span>
    </div>

    <div class="ribbon ribbon--ingredients">
      <svg viewBox="0 0 206 48" preserveAspectRatio="none" aria-hidden="true">
        <polygon points="0,0 206,0 188,24 206,48 0,48 18,24" fill="url(#gold-sheen)"/>
      </svg>
      <span class="ribbon__text">Ingredients</span>
    </div>

    <p class="ingredients">A complex blend of Pure Oils<br>including Marula, Sea Buckthorn,<br>Rosehip, Neroli, Evening primrose,<br>Argan, Calendula, Lavender, Jojoba,<br>Grapeseed, Baobab, Moringa and<br>Vitamin E oil.</p>

    <p class="producer">Produced by<br>Brasso Kettle Ltd<br>P.O box 7925-00300<br>Nairobi, Kenya<br>www.velumiorganics.example</p>
  </section>
</div>
</body>
</html>
```